Dental Office Needs- Flyer Design for Same Day Crowns

We need a flyer that will explain the benefits of the same day crown from the patient prospective. Not show pictures of the machine that makes the crowns. See attached material for content. The flyer should use the practices PMS colors of Green 562 and Blue 3025. The ad should say to the patient - I want to go this office and get my crown done there.
Updates

Project Deadline Extended Reason: The difference in the time zone between USA and Europe has caused issues. Minor changes still need to be worked out. Added Thursday, July 14, 2016

Target Market(s)

Dental Patients

Industry/Entity Type

Dental

Requirements
Must have
• Call to Action
• Business Address and Business Logo
• Classic Design
• images of a Happy 50 year old Couple
• Gives the benefits of the same day crown
Should not have
• No Images of tooth figures
• No before or after pictures

```html
<!DOCTYPE html>
<html lang="en">
<head>
<meta charset="utf-8">
<title>Same-Day Digital Restorations – Harbor Dental Care</title>
<link rel="stylesheet" href="https://fonts.googleapis.com/css2?family=Questrial&family=Pinyon+Script&family=Fira+Sans+Condensed:wght@600&family=Open+Sans:wght@400&display=swap">
<style>
  :root{
    --blue:#0f4c63;
    --green:#147d62;
    --green-bright:#179167;
    --paper:#ffffff;
  }
  *{margin:0;padding:0;box-sizing:border-box}
  html,body{width:1200px;height:1200px;overflow:hidden;background:var(--paper)}
  .flyer{position:relative;width:1200px;height:1200px;font-family:"Questrial",sans-serif;color:var(--green)}
  .band{position:absolute;background:var(--blue)}
  .band--top{left:38px;top:203px;width:375px;height:20px}
  .band--bottom{left:413px;top:976px;width:748px;height:20px}
  .photo{position:absolute}
  .photo--friends{left:413px;top:203px;width:748px;height:261px;
    background:linear-gradient(90deg,#6d7a3a 0%,#a7754f 30%,#e2b59c 50%,#b98064 70%,#7f8a48 100%)}
  .rule{position:absolute;left:413px;top:466px;width:748px;height:2px;background:var(--blue);opacity:.55}
  .photo--couple{left:40px;top:592px;width:373px;height:404px;
    background:linear-gradient(180deg,rgba(255,255,255,0) 0%,#b7b88a 20%,#c9b8a5 55%,#8da860 100%)}
  .intro{position:absolute;left:38px;top:312px;width:375px;text-align:center}
  .intro h1{font-weight:400;font-size:17.5px;color:var(--blue);letter-spacing:.2px;margin-bottom:30px}
  .intro p{font-size:16px;line-height:28.5px;letter-spacing:.6px;margin-bottom:11px}
  .para{position:absolute;font-size:15.5px;white-space:nowrap}
  .para--l{left:452px;line-height:22px;letter-spacing:1.1px}
  .para--r{line-height:25px;letter-spacing:.6px}
  .p1{top:498px;line-height:24px;letter-spacing:.7px}
  .p2{top:597px}
  .p3{top:714px}
  .p4{left:824px;top:498px}
  .p5{left:820px;top:678px}
  .cap{font-family:"Pinyon Script",cursive;font-size:40px;line-height:0;color:var(--blue);margin-right:1px;letter-spacing:0}
  .steps{position:absolute;left:413px;top:826px;width:748px;text-align:center}
  .steps h2{font-family:"Fira Sans Condensed",sans-serif;font-weight:600;font-size:25px;color:var(--green-bright);letter-spacing:.2px;margin-left:-16px}
  .steps ol{list-style:none;position:absolute;left:86px;top:40px;display:flex;gap:43px}
  .step{position:relative;width:80px;text-align:center}
  .step svg{display:block;width:80px;height:80px}
  .step span{display:block;margin-top:6px;font-family:"Open Sans",sans-serif;font-size:12px;color:var(--green)}
  .step:not(:last-child)::after{content:"";position:absolute;left:88px;top:40px;width:20px;height:2px;background:var(--blue)}
  .step:not(:last-child)::before{content:"";position:absolute;left:104px;top:35px;border-left:9px solid var(--blue);border-top:6px solid transparent;border-bottom:6px solid transparent}
</style>
</head>
<body>
<main class="flyer">
  <div class="band band--top"></div>

  <section class="intro">
    <h1>SAME-DAY DIGITAL RESTORATIONS.</h1>
    <p>Crowns, veneers and bridges that<br>happen in hours instead of days.</p>
    <p>Ask your dentist if digital dentistry<br>is right for you.</p>
  </section>

  <div class="photo photo--friends" role="img" aria-label="Photo of two smiling young women outdoors"></div>
  <div class="rule"></div>
  <div class="photo photo--couple" role="img" aria-label="Photo of a happy older couple embracing in a park"></div>

  <p class="para para--l p1"><span class="cap">H</span>arbor Dental Care is pleased to<br>offer you the Comfort and Convenience<br>of One Visit Dental Care.</p>
  <p class="para para--l p2"><span class="cap">W</span>e understand how hard it can be<br>to take off work or have someone<br>take care of the kids even once,<br>but twice??</p>
  <p class="para para--l p3"><span class="cap">N</span>ow with 3D CADCAM Technology,<br>we can digitally design and mill a<br>Customized, Ceramic Restoration<br>in one appointment.</p>

  <p class="para para--r p4"><span class="cap">R</span>estorative dentistry has evolved and<br>now, digital technology allows us to take<br>an impression of your teeth with a digital<br>scanner and create your restoration<br>right in our office.</p>
  <p class="para para--r p5"><span class="cap">W</span>e can match your existing teeth and<br>provide you with a filling, veneer, crown<br>or bridge using the most advanced non<br>-metal composite materials giving you a<br>beautiful smile and natural appearance.</p>

  <section class="steps">
    <h2>5 STEPS TO A BEAUTIFUL SMILE</h2>
    <ol>
      <li class="step">
        <svg viewBox="0 0 80 80" fill="none" stroke="#0f4c63" stroke-width="5"><rect x="3" y="3" width="74" height="74" rx="9"/><path d="M22 18h36v14H36v10h-8V26h-6z" stroke-width="4"/><path d="M32 42v22" stroke-width="4"/></svg>
        <span>Prep</span>
      </li>
      <li class="step">
        <svg viewBox="0 0 80 80" fill="none" stroke="#0f4c63" stroke-width="5"><rect x="3" y="3" width="74" height="74" rx="9"/><path d="M18 42l10-10h26a8 8 0 0 1 8 8" stroke-width="4"/><path d="M30 46l-8 10M34 46v12M38 46l6 10" stroke-width="2"/></svg>
        <span>Scan</span>
      </li>
      <li class="step">
        <svg viewBox="0 0 80 80" fill="none" stroke="#0f4c63" stroke-width="5"><rect x="3" y="3" width="74" height="74" rx="9"/><rect x="20" y="20" width="40" height="28" stroke-width="4"/><path d="M12 58h56" stroke-width="5"/><path d="M36 28h8v10h-8z" stroke-width="2"/></svg>
        <span>Design</span>
      </li>
      <li class="step">
        <svg viewBox="0 0 80 80" fill="none" stroke="#0f4c63" stroke-width="5"><rect x="3" y="3" width="74" height="74" rx="9"/><rect x="14" y="18" width="52" height="40" rx="5" stroke-width="4"/><rect x="30" y="18" width="14" height="10" fill="#179167" stroke="none"/><path d="M18 48h44" stroke-width="2"/></svg>
        <span>Mill</span>
      </li>
      <li class="step">
        <svg viewBox="0 0 80 80" fill="none" stroke="#0f4c63" stroke-width="5"><rect x="3" y="3" width="74" height="74" rx="9"/><path d="M16 36l16 12h30l-4 8H30L14 42zM36 56v10M28 66h18" stroke-width="4"/><circle cx="24" cy="30" r="4" fill="#0f4c63" stroke="none"/><path d="M36 16h20l6 6" stroke-width="3"/></svg>
        <span>Seat</span>
      </li>
    </ol>
  </section>

  <div class="band band--bottom"></div>
</main>
</body>
</html>
```